Mirela Dawn Business Card Design

I need a business card for my daughter. She has it all described in the file below. But it needs to be square in shape. http://www.mireladawn.example is her web site

Target Market(s)

18-35 year old women

Industry/Entity Type

Fashion

Contact Information for Business Card

Please look at the attached file as it has all the details.

Requirements
Must have
• Please look at the attached file as it has all the details.
Nice to have
Should not have

```html
<!DOCTYPE html>
<html lang="en">
<head>
<meta charset="utf-8">
<title>Mirela Dawn – Business Card</title>
<link rel="stylesheet" href="https://fonts.googleapis.com/css2?family=Abril+Fatface&family=Arimo:wght@700&family=Dancing+Script:wght@400;500&display=swap">
<style>
  :root {
    --pink: #f4a3c8;
    --pink-text: #f2a0c4;
    --ink: #000000;
    --paper: #ffffff;
    --marble-dark: #141414;
    --marble-mid: #2c2c2e;
  }
  * { margin: 0; padding: 0; box-sizing: border-box; }
  html, body {
    width: 1200px; height: 1200px; overflow: hidden;
    background: var(--paper);
  }
  .canvas { position: relative; width: 1200px; height: 1200px; }

  /* Front */
  .card-front {
    position: absolute; left: 54px; top: 333px; width: 535px; height: 534px;
    overflow: hidden;
  }
  .marble-fill {
    position: absolute; inset: 0;
    background:
      radial-gradient(ellipse at 40% 15%, #5a5a5a 0%, transparent 35%),
      radial-gradient(ellipse at 60% 60%, var(--marble-mid) 0%, transparent 60%),
      linear-gradient(160deg, #222 0%, var(--marble-dark) 55%, #1d1d1f 100%);
  }
  .brand-name {
    position: absolute; left: 124px; top: 522px - 333px;
  }
  .front-name {
    position: absolute; left: 70px; top: 186px;
    font-family: "Abril Fatface", "Playfair Display", serif;
    font-size: 55px; letter-spacing: 0.5px; line-height: 1;
    color: var(--pink-text); white-space: nowrap;
  }
  .front-rule {
    position: absolute; left: 70px; top: 265px; width: 240px; height: 4px;
    background: var(--paper);
  }
  .front-tagline {
    position: absolute; left: 68px; top: 288px;
    font-family: "Dancing Script", cursive;
    font-size: 66px; line-height: 1; color: var(--pink-text); white-space: nowrap;
  }

  /* Back */
  .card-back {
    position: absolute; left: 611px; top: 333px; width: 534px; height: 534px;
    background: var(--ink); padding: 29px;
  }
  .back-panel {
    position: relative; width: 100%; height: 100%; background: var(--pink);
    padding: 16px 16px 0 16px;
  }
  .role-banner {
    height: 59px; background: var(--ink); color: var(--paper);
    font-family: "Dancing Script", cursive; font-weight: 500;
    font-size: 25px; line-height: 59px; text-align: center; white-space: nowrap;
  }
  .contact-list { list-style: none; margin-top: 15px; }
  .contact-item {
    display: flex; align-items: center; height: 60px; padding-left: 24px;
  }
  .contact-icon {
    width: 42px; height: 42px; border-radius: 50%; background: var(--ink);
    flex: none; display: flex; align-items: center; justify-content: center;
  }
  .contact-text {
    margin-left: 24px;
    font-family: "Arimo", Arial, sans-serif; font-weight: 700;
    font-size: 32px; color: var(--ink); white-space: nowrap; letter-spacing: -0.3px;
  }
  .contact-text--long { font-size: 25px; }
</style>
</head>
<body>
<main class="canvas">
  <section class="card-front">
    <div class="marble-fill" role="img" aria-label="Black marble texture with white veins"></div>
    <h1 class="front-name">MIRELA DAWN</h1>
    <div class="front-rule"></div>
    <p class="front-tagline">fluent in fashion</p>
  </section>

  <section class="card-back">
    <div class="back-panel">
      <div class="role-banner">blogger &amp; youtuber // beauty • fashion • travel</div>
      <ul class="contact-list">
        <li class="contact-item"><span class="contact-icon"></span><span class="contact-text">@mireladawnxo</span></li>
        <li class="contact-item"><span class="contact-icon"></span><span class="contact-text">@mireladawnxo</span></li>
        <li class="contact-item"><span class="contact-icon"></span><span class="contact-text">@mireladawnxo</span></li>
        <li class="contact-item">
          <span class="contact-icon">
            <svg width="24" height="18" viewBox="0 0 24 18" aria-hidden="true">
              <rect x="1.5" y="1.5" width="21" height="15" rx="2" fill="none" stroke="#fff" stroke-width="2.5"/>
              <path d="M2 3 L12 10 L22 3" fill="none" stroke="#fff" stroke-width="2.5"/>
            </svg>
          </span>
          <span class="contact-text contact-text--long">mirela@mireladawn.example</span>
        </li>
        <li class="contact-item">
          <span class="contact-icon">
            <svg width="20" height="20" viewBox="0 0 20 20" aria-hidden="true">
              <path d="M10 2 L19 10 L16 10 L16 18 L12 18 L12 13 L8 13 L8 18 L4 18 L4 10 L1 10 Z" fill="#fff"/>
            </svg>
          </span>
          <span class="contact-text">mireladawn.example</span>
        </li>
        <li class="contact-item"><span class="contact-icon"></span><span class="contact-text">mireladawn</span></li>
      </ul>
    </div>
  </section>
</main>
</body>
</html>
```